New exciting tequila brand needs fun and attention drawing bottle label.

We need a design for on the glass bottle for a new tequila brand called "Mango Spin Tequila". It can be a label, or the decoration for the entire bottle.
The brand is called "Mango Spin" and is targeting a young party crowd.
I would like the visual to play with the image of a "tiger" & the idea of "up"side down.
In a bar the bottle needs to stand out, so it can be a very colourful design.

Good luck

Target Market(s)

young party crowd

Industry/Entity Type

Crowd

Colors
ec2027
fbed22
f37123
ffffff
f8ba93
fbf289

Requirements
Must have
• tiger
Nice to have
• play with the idea of upside down
Should not have
• have seen it before feeling

```html
<!DOCTYPE html>
<html lang="en">
<head>
<meta charset="utf-8">
<title>Mango Spin Tequila – label set</title>
<link rel="stylesheet" href="https://fonts.googleapis.com/css2?family=Anton&display=swap">
<style>
  :root {
    --red: #e52228;
    --yellow: #fdd900;
    --black: #1d1d1b;
    --white: #ffffff;
    --paper: #ffffff;
  }
  * { box-sizing: border-box; margin: 0; padding: 0; }
  html, body {
    width: 1200px;
    height: 597px;
    overflow: hidden;
    background: var(--paper);
  }
  .label-sheet {
    width: 1200px;
    height: 597px;
    display: grid;
    grid-template-columns: repeat(8, 1fr);
    grid-template-rows: repeat(2, 1fr);
    gap: 1px;
    font-family: "Anton", "Impact", sans-serif;
  }
  .label {
    position: relative;
    overflow: hidden;
    border-radius: 4px;
    background: var(--bg);
  }
  .label--flipped { transform: rotate(180deg); }

  .is-bg-red    { --bg: var(--red); }
  .is-bg-yellow { --bg: var(--yellow); }
  .is-bg-black  { --bg: var(--black); }
  .is-ink-red    { --ink: var(--red); }
  .is-ink-yellow { --ink: var(--yellow); }
  .is-ink-black  { --ink: var(--black); }
  .is-tag-red    { --tag: var(--red); }
  .is-tag-yellow { --tag: var(--yellow); }
  .is-tag-black  { --tag: var(--black); }
  .is-tag-white  { --tag: var(--white); }
  .is-beast-red   { --beast: var(--red); }
  .is-beast-black { --beast: var(--black); }
  .is-beast-white { --beast: var(--white); }

  .label__tag {
    position: absolute;
    top: 14px;
    right: 16px;
    font-size: 10px;
    letter-spacing: 3px;
    line-height: 1;
    color: var(--tag);
  }
  .label__name {
    position: absolute;
    top: 24px;
    left: 12px;
    width: 126px;
    color: var(--ink);
    text-transform: uppercase;
  }
  .label__name-line {
    display: block;
    line-height: 1;
    transform-origin: top left;
  }
  .label__name-line--top {
    font-size: 41px;
    transform: scaleY(1.3);
  }
  .label__name-line--bottom {
    margin-top: 12px;
    font-size: 60px;
    letter-spacing: -1px;
    transform: scaleY(1.5);
  }
  .label__tiger {
    position: absolute;
    left: 14px;
    bottom: 6px;
    width: 122px;
    height: 122px;
    background: var(--beast);
    border-radius: 45% 55% 40% 50% / 55% 45% 50% 40%;
    opacity: 0.9;
  }
</style>
</head>
<body>
<main class="label-sheet">
  <!-- top row: turned labels -->
  <section class="label label--flipped is-bg-red is-ink-yellow is-tag-yellow is-beast-black">
    <span class="label__tag">TEQUILA</span>
    <h2 class="label__name"><span class="label__name-line label__name-line--top">Mango</span><span class="label__name-line label__name-line--bottom">Spin</span></h2>
    <div class="label__tiger" role="img" aria-label="Crouching tiger illustration in halftone print"></div>
  </section>
  <section class="label label--flipped is-bg-yellow is-ink-red is-tag-red is-beast-black">
    <span class="label__tag">TEQUILA</span>
    <h2 class="label__name"><span class="label__name-line label__name-line--top">Mango</span><span class="label__name-line label__name-line--bottom">Spin</span></h2>
    <div class="label__tiger" role="img" aria-label="Crouching tiger illustration in halftone print"></div>
  </section>
  <section class="label label--flipped is-bg-red is-ink-black is-tag-black is-beast-black">
    <span class="label__tag">TEQUILA</span>
    <h2 class="label__name"><span class="label__name-line label__name-line--top">Mango</span><span class="label__name-line label__name-line--bottom">Spin</span></h2>
    <div class="label__tiger" role="img" aria-label="Crouching tiger illustration in halftone print"></div>
  </section>
  <section class="label label--flipped is-bg-black is-ink-red is-tag-white is-beast-white">
    <span class="label__tag">TEQUILA</span>
    <h2 class="label__name"><span class="label__name-line label__name-line--top">Mango</span><span class="label__name-line label__name-line--bottom">Spin</span></h2>
    <div class="label__tiger" role="img" aria-label="Crouching tiger illustration in halftone print"></div>
  </section>
  <section class="label label--flipped is-bg-red is-ink-yellow is-tag-yellow is-beast-black">
    <span class="label__tag">TEQUILA</span>
    <h2 class="label__name"><span class="label__name-line label__name-line--top">Mango</span><span class="label__name-line label__name-line--bottom">Spin</span></h2>
    <div class="label__tiger" role="img" aria-label="Crouching tiger illustration in halftone print"></div>
  </section>
  <section class="label label--flipped is-bg-yellow is-ink-red is-tag-red is-beast-black">
    <span class="label__tag">TEQUILA</span>
    <h2 class="label__name"><span class="label__name-line label__name-line--top">Mango</span><span class="label__name-line label__name-line--bottom">Spin</span></h2>
    <div class="label__tiger" role="img" aria-label="Crouching tiger illustration in halftone print"></div>
  </section>
  <section class="label label--flipped is-bg-red is-ink-yellow is-tag-yellow is-beast-black">
    <span class="label__tag">TEQUILA</span>
    <h2 class="label__name"><span class="label__name-line label__name-line--top">Mango</span><span class="label__name-line label__name-line--bottom">Spin</span></h2>
    <div class="label__tiger" role="img" aria-label="Crouching tiger illustration in halftone print"></div>
  </section>
  <section class="label label--flipped is-bg-black is-ink-red is-tag-white is-beast-white">
    <span class="label__tag">TEQUILA</span>
    <h2 class="label__name"><span class="label__name-line label__name-line--top">Mango</span><span class="label__name-line label__name-line--bottom">Spin</span></h2>
    <div class="label__tiger" role="img" aria-label="Crouching tiger illustration in halftone print"></div>
  </section>

  <!-- bottom row: upright labels -->
  <section class="label is-bg-yellow is-ink-black is-tag-red is-beast-red">
    <span class="label__tag">TEQUILA</span>
    <h2 class="label__name"><span class="label__name-line label__name-line--top">Mango</span><span class="label__name-line label__name-line--bottom">Spin</span></h2>
    <div class="label__tiger" role="img" aria-label="Upside-down tiger illustration in halftone print"></div>
  </section>
  <section class="label is-bg-red is-ink-black is-tag-yellow is-beast-white">
    <span class="label__tag">TEQUILA</span>
    <h2 class="label__name"><span class="label__name-line label__name-line--top">Mango</span><span class="label__name-line label__name-line--bottom">Spin</span></h2>
    <div class="label__tiger" role="img" aria-label="Upside-down tiger illustration in halftone print"></div>
  </section>
  <section class="label is-bg-yellow is-ink-red is-tag-red is-beast-black">
    <span class="label__tag">TEQUILA</span>
    <h2 class="label__name"><span class="label__name-line label__name-line--top">Mango</span><span class="label__name-line label__name-line--bottom">Spin</span></h2>
    <div class="label__tiger" role="img" aria-label="Upside-down tiger illustration in halftone print"></div>
  </section>
  <section class="label is-bg-red is-ink-yellow is-tag-yellow is-beast-black">
    <span class="label__tag">TEQUILA</span>
    <h2 class="label__name"><span class="label__name-line label__name-line--top">Mango</span><span class="label__name-line label__name-line--bottom">Spin</span></h2>
    <div class="label__tiger" role="img" aria-label="Upside-down tiger illustration in halftone print"></div>
  </section>
  <section class="label is-bg-yellow is-ink-black is-tag-red is-beast-red">
    <span class="label__tag">TEQUILA</span>
    <h2 class="label__name"><span class="label__name-line label__name-line--top">Mango</span><span class="label__name-line label__name-line--bottom">Spin</span></h2>
    <div class="label__tiger" role="img" aria-label="Upside-down tiger illustration in halftone print"></div>
  </section>
  <section class="label is-bg-red is-ink-black is-tag-yellow is-beast-black">
    <span class="label__tag">TEQUILA</span>
    <h2 class="label__name"><span class="label__name-line label__name-line--top">Mango</span><span class="label__name-line label__name-line--bottom">Spin</span></h2>
    <div class="label__tiger" role="img" aria-label="Upside-down tiger illustration in halftone print"></div>
  </section>
  <section class="label is-bg-yellow is-ink-red is-tag-red is-beast-black">
    <span class="label__tag">TEQUILA</span>
    <h2 class="label__name"><span class="label__name-line label__name-line--top">Mango</span><span class="label__name-line label__name-line--bottom">Spin</span></h2>
    <div class="label__tiger" role="img" aria-label="Upside-down tiger illustration in halftone print"></div>
  </section>
  <section class="label is-bg-red is-ink-black is-tag-yellow is-beast-white">
    <span class="label__tag">TEQUILA</span>
    <h2 class="label__name"><span class="label__name-line label__name-line--top">Mango</span><span class="label__name-line label__name-line--bottom">Spin</span></h2>
    <div class="label__tiger" role="img" aria-label="Upside-down tiger illustration in halftone print"></div>
  </section>
</main>
</body>
</html>
```